Recreating a Opt-in for a FREE BOOK for brides.

I need to have an opt-in box recreated to make brides want to get my free book. The opt-in message is already on the mock website. It needs to look graphically pleasing in the colors being used, but bold enough to grab the viewers attention. I am including the link to the website where the graphic needs to be re-created. You'll notice there are two areas where the graphics need to go.

Target Market(s)

Brides

Requirements
Must have
• Begin by looking at the website..http://qvotrl.com/zu-pim/
On the homepage is the current "A Gift For You" graphic. (I have included an image of the home page for the circled area that needs to be recreated.) As of now, the graphics looks amateurish. It needs your professional upgrade. The image of the book has also been uploaded as a file for you to use.

In addition, on the FAQ page, there is a graphic that has been created to fit that area of the page to get the book (circled area of the graphic has been uploaded). I need to have the same graphic you are creating for the home page, but adjust it to be placed on this page. When you recreate the graphic for the FAQ page, there are 2 changes to the text:

1. Change the word "Receive" to "Download." (The rest of the sentence should stay the same.)
2. Delete the entire sentence "Or, pay $17.95 at zellora or tolliver and wrenfield by clicking here.
Nice to have
• Normal file formats such as jpeg, photoshop or ai are fine.

```html
<!DOCTYPE html>
<html lang="en">
<head>
<meta charset="utf-8">
<title>A Gift for You – Brides Guide Opt-in</title>
<link rel="stylesheet" href="https://fonts.googleapis.com/css2?family=Great+Vibes&family=Lexend:wght@300;600&family=Montserrat:wght@700&display=swap">
<style>
  :root {
    --paper: #ffffff;
    --coral: #f27c76;
    --plum: #4f2479;
    --book-light: #f1efee;
    --book-teal: #8cc7c9;
    --shadow: rgba(60, 40, 50, 0.18);
  }
  * { margin: 0; padding: 0; box-sizing: border-box; }
  html, body {
    width: 1200px;
    height: 865px;
    overflow: hidden;
    background: var(--paper);
  }
  .optin {
    position: relative;
    width: 1200px;
    height: 865px;
    background: var(--paper);
  }
  .optin__art {
    position: absolute;
    inset: 0;
  }
  .gift-script {
    font-family: "Great Vibes", cursive;
    fill: var(--coral);
  }
  .book-title {
    position: absolute;
    left: 80px;
    top: 520px;
    width: 500px;
    text-align: center;
    font-family: "Lexend", sans-serif;
    font-weight: 300;
    font-size: 35px;
    line-height: 50px;
    color: var(--plum);
    letter-spacing: -0.3px;
  }
  .book-title strong { font-weight: 600; }
  .cta {
    position: absolute;
    left: 82px;
    top: 672px;
    width: 492px;
    height: 58px;
  }
  .cta__rule {
    position: absolute;
    left: 0;
    right: 0;
    top: 27px;
    height: 2px;
    background: var(--coral);
  }
  .cta__button {
    position: absolute;
    left: 104px;
    top: 0;
    width: 268px;
    height: 58px;
    border: 2px solid var(--plum);
    border-radius: 29px;
    background: var(--paper);
    padding: 4px;
    box-shadow: 0 14px 10px -8px var(--shadow);
  }
  .cta__label {
    display: flex;
    align-items: center;
    justify-content: center;
    width: 100%;
    height: 100%;
    border-radius: 25px;
    background: var(--coral);
    font-family: "Montserrat", sans-serif;
    font-weight: 700;
    font-size: 30px;
    color: var(--paper);
    letter-spacing: -0.5px;
    text-decoration: none;
  }
</style>
</head>
<body>
  <main class="optin">
    <svg class="optin__art" width="1200" height="865" viewBox="0 0 1200 865">
      <defs>
        <radialGradient id="blush-wash" cx="50%" cy="50%" r="50%">
          <stop offset="0%" stop-color="#f4e1dc"/>
          <stop offset="70%" stop-color="#f9eeeb"/>
          <stop offset="100%" stop-color="#ffffff" stop-opacity="0"/>
        </radialGradient>
        <linearGradient id="book-cover" x1="0" y1="0" x2="1" y2="1">
          <stop offset="0%" stop-color="#f3f1ef"/>
          <stop offset="45%" stop-color="#ece3e0"/>
          <stop offset="75%" stop-color="#c9dedd"/>
          <stop offset="100%" stop-color="#eeeeee"/>
        </linearGradient>
        <radialGradient id="book-shadow" cx="50%" cy="50%" r="50%">
          <stop offset="0%" stop-color="#000" stop-opacity="0.14"/>
          <stop offset="100%" stop-color="#000" stop-opacity="0"/>
        </radialGradient>
      </defs>

      <ellipse class="brush-wash" role="img" aria-label="Soft blush paint strokes with berry branch sprigs behind the book"
               cx="880" cy="430" rx="320" ry="250" fill="url(#blush-wash)"/>

      <ellipse cx="900" cy="728" rx="280" ry="24" fill="url(#book-shadow)"/>

      <g class="book-mockup" role="img" aria-label="Book cover for the brides wedding cake guide: a couple in a soft embrace and a tiered white wedding cake with a pink rose">
        <polygon points="632,164 982,150 972,696 632,743" fill="url(#book-cover)"/>
        <polygon points="632,164 663,163 663,739 632,743" fill="var(--book-light)"/>
        <polygon points="663,686 973,638 973,648 663,696" fill="var(--book-teal)"/>
      </g>

      <g class="gift-script">
        <text x="138" y="200" font-size="62">a</text>
        <text x="180" y="262" font-size="180">Gift</text>
        <text x="412" y="290" font-size="82">for</text>
        <text x="300" y="410" font-size="150">You</text>
      </g>
    </svg>

    <h1 class="book-title">The <strong>Perfect Brides Guide</strong><br>for Picking a <strong>Wedding Cake</strong></h1>

    <div class="cta">
      <span class="cta__rule"></span>
      <div class="cta__button"><a class="cta__label" href="#">GET IT NOW!</a></div>
    </div>
  </main>
</body>
</html>
```